依頼概要
■依頼の目的/概要
和歌山県で自然農法の農家をしています「坂口青葉ファーム」と申します。
弊社が販売している「大麦シリアル」のラベルデザインをお願いします。

■依頼詳細
今回は弊社が販売する自然農法の「大麦シリアル」のラベルのデザインをお願いします。

特徴
●原材料の大麦は、完全無肥料・無農薬の自然農法栽培のものを100%使用していますので健康志向の方にお勧めで安心して食べて頂けます。
●全て自社「坂口青葉ファーム」産の六条大麦を使用しています。
●今話題になっている、五穀の王様である「大麦」が毎日手軽に食べられるシリアルになりました。
●朝食やおやつなどに手軽に食べれて健康的です。
●牛乳・豆乳・ヨーグルトなどをかけて食べて頂けます。
●お好みで果物やドライフルーツ、ナッツなどを添えて食べると更に健康的です。
●何もかけずにポン菓子のようにも食べることができます。砂糖などで甘味を付けていないのでお子様のおやつにも安心です。
●大麦は水溶性食物繊維が豊富でとても体にいい食べ物です。

■その他要望
●自社のロゴマークをラベルデザインの中にいれてください。
ロゴマークは添付してあります。
●パッケージは
透明のスタンドチャック式のものです。(表面透明、裏面は白)
大きさはチャックの部分まで含めて
縦230㎜×横160㎜になります。(添付写真あります)
●添付写真に大麦シリアルの写真があります。使えそうなら使って下さい。
独自の写真を使って頂いても結構です。

●表記に関してですが
「無肥料・無農薬」とは法律上書くことができません。
「無肥料・無農薬」×→「肥料・農薬不使用」○と表記してください。
「自然農法」という言葉も登録商標の関係で使えません。
「自然農法」×→「自然栽培」とお願いします。
●朝から健康のために続けたくなるようなデザインをお願いいたします。
デザイナーの皆様、どうぞよろしくお願いいたします。

その他何かご不明な点がございましたら、お気軽にご質問下さい。
よろしくお願いいたします。
■ 選んだ理由

バランスが取れていて分かりやすい
必要な説明が明記されている
写真を効果的に使っている

■ 提案者全員のお礼・コメント

素晴らしいご提案を頂きありがとうございました。
今後ともどうぞよろしくお願いします。

```html
<!DOCTYPE html>
<html lang="ja">
<head>
<meta charset="UTF-8">
<title>大麦シリアル ラベル</title>
<link rel="stylesheet" href="https://fonts.googleapis.com/css2?family=Noto+Serif+JP:wght@500;700;900&family=Roboto+Slab:wght@700&family=Noto+Sans+JP:wght@500&display=swap">
<style>
  :root {
    --ink: #3b2a1f;
    --label: #ffffff;
    --pouch-top: #eef0ee;
    --grain-light: #d8b98c;
    --grain-mid: #b8915f;
    --grain-dark: #8a6440;
  }
  html, body {
    margin: 0;
    padding: 0;
    width: 900px;
    height: 1200px;
    overflow: hidden;
    background: #ffffff;
  }
  .pouch {
    position: relative;
    width: 900px;
    height: 1200px;
    overflow: hidden;
    background: var(--pouch-top);
  }
  .zipper-line {
    position: absolute;
    left: 0; right: 0;
    top: 130px;
    height: 4px;
    background: #d6d9d6;
  }
  .cereal-fill {
    position: absolute;
    left: 0; right: 0;
    top: 250px;
    bottom: 0;
    background:
      radial-gradient(ellipse at 30% 20%, var(--grain-light) 0%, transparent 55%),
      radial-gradient(ellipse at 75% 60%, var(--grain-light) 0%, transparent 50%),
      linear-gradient(180deg, var(--grain-mid) 0%, var(--grain-light) 45%, var(--grain-mid) 80%, var(--grain-dark) 100%);
  }
  .label {
    position: absolute;
    left: 130px;
    top: 460px;
    width: 640px;
    height: 720px;
    border-radius: 50%;
    background: var(--label);
    color: var(--ink);
    text-align: center;
  }
  .arc-copy {
    position: absolute;
    left: 0; top: 0;
    width: 640px; height: 720px;
  }
  .arc-copy text {
    font-family: "Noto Serif JP", serif;
    font-weight: 700;
    font-size: 30px;
    letter-spacing: 4px;
    fill: var(--ink);
  }
  .title-main {
    position: absolute;
    left: 0; right: 0;
    top: 100px;
    margin: 0;
    font-family: "Noto Serif JP", serif;
    font-weight: 900;
    font-size: 150px;
    line-height: 1;
    letter-spacing: 6px;
  }
  .title-sub {
    position: absolute;
    left: 0; right: 0;
    top: 268px;
    margin: 0;
    font-family: "Noto Serif JP", serif;
    font-weight: 900;
    font-size: 118px;
    line-height: 1;
    letter-spacing: 2px;
  }
  .product-band {
    position: absolute;
    left: 40px; right: 40px;
    top: 410px;
    padding: 10px 0 8px;
    border-top: 3px solid var(--ink);
    border-bottom: 3px solid var(--ink);
    font-family: "Roboto Slab", serif;
    font-weight: 700;
    font-size: 38px;
    letter-spacing: 3px;
    line-height: 1.1;
  }
  .claim {
    position: absolute;
    left: 0; right: 0;
    top: 488px;
    font-family: "Noto Serif JP", serif;
    font-weight: 700;
    font-size: 32px;
    letter-spacing: 2px;
  }
  .description {
    position: absolute;
    left: 90px; right: 90px;
    top: 548px;
    margin: 0;
    font-family: "Noto Sans JP", sans-serif;
    font-weight: 500;
    font-size: 18px;
    line-height: 1.35;
  }
  .brand {
    position: absolute;
    left: 0; right: 0;
    top: 650px;
    display: flex;
    justify-content: center;
    align-items: center;
    gap: 8px;
    font-family: "Noto Serif JP", serif;
    font-weight: 700;
    font-size: 20px;
    letter-spacing: 3px;
  }
  .brand-dot {
    width: 12px;
    height: 12px;
    border-radius: 50%;
    background: var(--ink);
  }
</style>
</head>
<body>
  <div class="pouch">
    <div class="zipper-line"></div>
    <div class="cereal-fill" role="img" aria-label="透明な袋越しに見えるパフ大麦シリアル"></div>

    <div class="label">
      <svg class="arc-copy" viewBox="0 0 640 720" aria-hidden="false">
        <defs>
          <path id="label-arc" d="M 58 360 A 262 322 0 0 1 582 360" fill="none"/>
        </defs>
        <text><textPath href="#label-arc" startOffset="50%" text-anchor="middle">自然栽培の六条大麦を使用</textPath></text>
      </svg>
      <h1 class="title-main">大麦</h1>
      <p class="title-sub">シリアル</p>
      <div class="product-band">PUFFED BARLEY CEREAL</div>
      <div class="claim">肥料・農薬不使用</div>
      <p class="description">The barley, the king of the five grains,<br>is now a hot topic cereal<br>that can be easily eaten every day.</p>
      <div class="brand"><span class="brand-dot"></span>AOBA</div>
    </div>
  </div>
</body>
</html>
```